Vorn Apparel Brochure Project

Looking for a brochure to send out with samples of our apparel. The name of our company is Vorn Apparel and we are distributors for 7.42. I have attached an older 7.42 brochure. I would like the brochure to be regular paper size with no folds.

Target Market(s)

Buyers working for large U.S. retail stores

Colors

Designer to choose colors to be used in the design.

Requirements
Must have
• Must look sleek and professional.

```html
<!DOCTYPE html>
<html lang="en">
<head>
<meta charset="utf-8">
<title>Vorn Apparel Brochure</title>
<link href="https://fonts.googleapis.com/css2?family=Oswald:wght@500;600;700&family=Roboto:wght@400&display=swap" rel="stylesheet">
<style>
  :root {
    --page-bg: #4a4a4a;
    --brand-red: #8b1a1b;
    --brand-red-deep: #7a1518;
    --band-grey: #e6e6e6;
    --text-light: #ffffff;
  }
  * { margin: 0; padding: 0; box-sizing: border-box; }
  html, body {
    width: 1200px;
    height: 1146px;
    overflow: hidden;
    background: var(--page-bg);
  }
  .brochure {
    position: absolute;
    left: 195px;
    top: 0;
    width: 810px;
    height: 1146px;
    overflow: hidden;
    font-family: "Roboto", sans-serif;
  }
  .masthead {
    position: absolute;
    left: 0; top: 0;
    width: 100%;
    height: 141px;
    background: var(--brand-red);
  }
  .masthead .mark {
    position: absolute;
    left: 207px; top: 24px;
    width: 90px; height: 90px;
    border: 2px solid var(--text-light);
    border-radius: 50%;
  }
  .masthead .brand-name {
    position: absolute;
    left: 327px; top: 38px;
    font-family: "Roboto", sans-serif;
    font-weight: 400;
    font-size: 48px;
    line-height: 56px;
    color: var(--text-light);
  }
  .hero-photo {
    position: absolute;
    left: 0; top: 141px;
    width: 100%;
    height: 1005px;
    background: linear-gradient(180deg,
      #5f7a3e 0%, #4f6a33 25%, #4a5230 42%,
      #6a3a32 60%, #7b3b38 78%, #8a4a46 100%);
  }
  .story {
    position: absolute;
    left: 39px; top: 494px;
    width: 732px;
    color: var(--text-light);
    font-size: 18.2px;
    line-height: 23.6px;
    text-align: justify;
  }
  .story p + p { margin-top: 23.6px; }
  .contact-band {
    position: absolute;
    left: 0; top: 977px;
    width: 100%;
    height: 85px;
    background: var(--band-grey);
    font-family: "Oswald", sans-serif;
    font-weight: 500;
    color: var(--brand-red);
    text-transform: uppercase;
    text-align: center;
    font-size: 15.5px;
    line-height: 21px;
    padding-top: 21px;
    letter-spacing: -0.2px;
  }
  .contact-band .detail {
    font-weight: 700;
    font-size: 20px;
    text-transform: none;
  }
  .social-links {
    position: absolute;
    left: 0; top: 1088px;
    width: 100%;
    display: flex;
    justify-content: center;
    gap: 3px;
  }
  .social-links span {
    width: 29px; height: 29px;
    border: 1.5px solid var(--text-light);
    border-radius: 50%;
  }
</style>
</head>
<body>
  <main class="brochure">
    <div class="hero-photo" role="img" aria-label="Photo of a model in a sleeveless navy khadi dress standing in a sunny garden beside a wrought-iron fence, tinted red toward the bottom"></div>

    <header class="masthead">
      <div class="mark"></div>
      <div class="brand-name">vorn apparel</div>
    </header>

    <section class="story">
      <p>We proudlypresent the finest artisanal luxury, hand-spun and hand-woven (known as “khadi) fabric products, emphasizing the link between farmers, weavers, vegetable dyers and block printing traditions. This result is a coherent and meaningful fashion garment line that creates grounds for ethical products.</p>
      <p>Our clothes are 100% handmade by 7.42 artisans and we select the finest of fabrics for our designs including khadi denim, kala cotton (all organic), 200 count khadi cotton, silk and ahimsa silk.&nbsp; All cotton fabric used by 7.42 is 100% khadi cotton and dyed in 100% natural dyes.</p>
      <p>Khadi is an ideal choice for green and ethical clothing. Made from cotton, silk, wool and other natural fibers, these fabrics have been in existence for hundreds of years.Today the production of khadi provides sustenance to millions of people in India. About eighty percent of khadi artisans are women often from some of the poorest communities in the country.</p>
      <p>Our fabric simply looks beautiful. It is a labor of love. It’s about human beings working with nature and transforming natural materials into beautiful wearable clothing.</p>
    </section>

    <section class="contact-band">
      We would love to talk with you about supplying our artisan products to your establishment.<br>
      Please feel free to contact me via email at <span class="detail">studio@vornapparel.com</span> or cell phone at <span class="detail">555-014-2742.</span>
    </section>

    <nav class="social-links" aria-label="Social media">
      <span></span><span></span><span></span>
    </nav>
  </main>
</body>
</html>
```